Investment Business - Biz Card Design

Using the attached logo files, please create a superior business card design for Brantwell Holdings.

The "back" of the card should feature the logo (either in colour, or white/black over a feature colour)

The "front" of the card should feature: name, email, and phone

The design should be minimal and clean.

Target Market(s)

Business owners who need our investment services.

Industry/Entity Type

Business

```html
<!DOCTYPE html>
<html lang="en">
<head>
<meta charset="utf-8">
<title>Brantwell Holdings – Business Card</title>
<link rel="stylesheet" href="https://fonts.googleapis.com/css2?family=Lato:wght@400;700;900&display=swap">
<style>
  :root {
    --backdrop: #e9eaec;
    --paper: #ffffff;
    --navy: #2b3c97;
    --sky: #25a7df;
    --ink-light: #ffffff;
    --shadow: rgba(20, 24, 40, 0.18);
  }
  * { box-sizing: border-box; margin: 0; padding: 0; }
  html, body {
    width: 1200px;
    height: 926px;
    overflow: hidden;
    background: var(--backdrop);
    font-family: "Lato", Arial, sans-serif;
  }
  .canvas {
    width: 1200px;
    height: 926px;
    display: flex;
    flex-direction: column;
    align-items: center;
    justify-content: center;
    gap: 42px;
  }
  .card {
    position: relative;
    width: 700px;
    height: 400px;
    background: var(--paper);
    box-shadow: 0 10px 28px var(--shadow);
    overflow: hidden;
  }

  /* Back side: brand name */
  .card-back {
    display: flex;
    align-items: center;
    justify-content: center;
    gap: 22px;
  }
  .brand-square {
    width: 34px;
    height: 34px;
    background: var(--navy);
  }
  .brand-name {
    color: var(--navy);
    font-weight: 900;
    font-size: 44px;
    letter-spacing: 3px;
    text-transform: uppercase;
  }

  /* Front side: brand + contact panel */
  .card-front .brand-block {
    position: absolute;
    left: 44px;
    top: 118px;
    width: 240px;
  }
  .card-front .brand-name {
    font-size: 34px;
    line-height: 1.1;
    letter-spacing: 2px;
  }
  .contact-panel {
    position: absolute;
    top: 0;
    right: 0;
    width: 400px;
    height: 400px;
  }
  .contact-panel svg { position: absolute; inset: 0; }
  .contact-details {
    position: absolute;
    left: 44px;
    bottom: 70px;
    color: var(--ink-light);
  }
  .person-name {
    font-weight: 700;
    font-size: 26px;
    letter-spacing: 2.5px;
    text-transform: uppercase;
    margin-bottom: 14px;
  }
  .contact-line {
    font-size: 17px;
    line-height: 1.35;
    letter-spacing: 0.5px;
  }
</style>
</head>
<body>
<main class="canvas">
  <section class="card card-back" aria-label="Card back">
    <span class="brand-square" aria-hidden="true"></span>
    <span class="brand-name">Brantwell Holdings</span>
  </section>

  <section class="card card-front" aria-label="Card front">
    <div class="brand-block">
      <span class="brand-name">Brantwell Holdings</span>
    </div>
    <div class="contact-panel">
      <svg width="400" height="400" viewBox="0 0 400 400" aria-hidden="true">
        <path d="M24 0 H400 V400 H24 V104 Q24 92 12 88 L0 84 L12 80 Q24 76 24 64 Z" fill="var(--sky)"/>
      </svg>
      <div class="contact-details">
        <p class="person-name">John Doe</p>
        <p class="contact-line">johndoe@brantwellholdings.com</p>
        <p class="contact-line">brantwellholdings.com</p>
        <p class="contact-line">000 - 1234 - 5678</p>
      </div>
    </div>
  </section>
</main>
</body>
</html>
```